Skatepark, and Teenage Music/Recreation Venue needs logo, business card and letterhead. Website desi

- Logo, Letterhead & Business Card design for a new start Skatepark and Youth Venue called "The Kelp" (Pty.Ltd company) in Australia.

- Website and App design will follow within 6-months.

- Facility centered around world class skatepark which incorporates the use of innovative technology applications to enhance consumer experience, it will also provide a live entertainment & music venue for teenagers.

- Appearance should appeal to the 'mature' teenage population, the aim is provide an excellent membership experience which can be associated with the club brand.

Overall the design should communicate:
Excitement, energy, exclusivity and style

- Clean and modern fonts and styling preferred.
- Logos the I personally like: Brimlow, Corvessane, (but they don't have to be round!)
- Generally I prefer understated business cards that are subtlety/elegently distinct
- ideally the logo would be expected to standalone if no text were available. (if that makes sense?)

Business

The Kelp

```html
<!DOCTYPE html>
<html lang="en">
<head>
<meta charset="utf-8">
<title>The Kelp — Stationery</title>
<link rel="stylesheet" href="https://fonts.googleapis.com/css2?family=Questrial&display=swap">
<style>
  :root {
    --backdrop: #e7e7e7;
    --paper: #ffffff;
    --ink: #3d3a3a;
    --accent: #d4771c;
    --card-dark: #1f1b1a;
    --watermark: #e4e2e1;
    --font-text: "Questrial", "Century Gothic", sans-serif;
  }
  * { margin: 0; padding: 0; box-sizing: border-box; }
  html, body { width: 1200px; height: 800px; overflow: hidden; }
  body {
    position: relative;
    background: var(--backdrop);
    font-family: var(--font-text);
    color: var(--ink);
  }

  .wordmark {
    position: absolute;
    display: flex;
    align-items: center;
    white-space: nowrap;
    font-family: var(--font-text);
    font-weight: 400;
    line-height: 1;
  }
  .wordmark__dot {
    display: inline-block;
    border-radius: 50%;
    background: var(--accent);
  }

  .logo-display { left: 180px; top: 125px; font-size: 82px; color: var(--ink); gap: 18px; }
  .logo-display .wordmark__dot { width: 16px; height: 16px; }

  .card {
    position: absolute;
    left: 116px;
    width: 449px;
    height: 211px;
  }
  .card--front { top: 336px; background: var(--paper); }
  .card--back { top: 563px; background: var(--card-dark); }

  .card--front .wordmark { left: 116px; top: 22px; font-size: 40px; color: var(--ink); gap: 9px; }
  .card--front .wordmark__dot { width: 8px; height: 8px; }

  .card__person {
    position: absolute;
    left: 41px;
    top: 143px;
    font-size: 16px;
    line-height: 20px;
    color: var(--accent);
  }
  .card__divider {
    position: absolute;
    left: 211px;
    top: 104px;
    width: 2px;
    height: 78px;
    background: var(--accent);
  }
  .card__contact {
    position: absolute;
    left: 226px;
    top: 106px;
    font-size: 15.5px;
    line-height: 20.5px;
    list-style: none;
  }
  .label { color: var(--accent); }
  .value { color: var(--ink); font-size: 14px; }
  .card__contact .phone { font-size: 15.5px; }

  .card--back .wordmark {
    left: 0; right: 0; top: 70px;
    justify-content: center;
    font-size: 62px;
    color: var(--paper);
  }

  .letterhead {
    position: absolute;
    left: 598px;
    top: 53px;
    width: 549px;
    height: 723px;
    background: var(--paper);
  }
  .letterhead__logo { right: 34px; top: 38px; font-size: 48px; color: var(--ink); gap: 10px; }
  .letterhead__logo .wordmark__dot { width: 9px; height: 9px; }
  .letterhead__watermark {
    left: 0; right: 0; top: 265px;
    justify-content: center;
    font-size: 124px;
    color: var(--watermark);
  }
  .letterhead__footer {
    position: absolute;
    left: 0; right: 0;
    bottom: 2px;
    text-align: center;
    font-size: 13.5px;
    line-height: 21px;
  }
  .letterhead__footer .value { font-size: 13.5px; }
  .letterhead__footer .item + .item { margin-left: 6px; }
</style>
</head>
<body>

  <div class="wordmark logo-display">
    <span class="wordmark__dot"></span><span>The Kelp</span>
  </div>

  <section class="card card--front">
    <div class="wordmark">
      <span class="wordmark__dot"></span><span>The Kelp</span>
    </div>
    <p class="card__person">Your Name<br>Designation</p>
    <span class="card__divider"></span>
    <ul class="card__contact">
      <li class="label">Address:</li>
      <li><span class="label">Ph.:</span><span class="value phone">+91 9810552743</span></li>
      <li><span class="label">eMail:</span><span class="value">hello@thekelp.com</span></li>
      <li><span class="label">Web:</span> <span class="value">www.thekelp.com</span></li>
    </ul>
  </section>

  <section class="card card--back">
    <div class="wordmark"><span>The Kelp</span></div>
  </section>

  <section class="letterhead">
    <div class="wordmark letterhead__logo">
      <span class="wordmark__dot"></span><span>The Kelp</span>
    </div>
    <div class="wordmark letterhead__watermark" aria-hidden="true"><span>The Kelp</span></div>
    <footer class="letterhead__footer">
      <div class="value">Address:</div>
      <div>
        <span class="item"><span class="label">Ph.:</span> <span class="value">+91 9810552743</span></span>
        <span class="item"><span class="label">eMail:</span> <span class="value">hello@thekelp.com</span></span>
        <span class="item"><span class="label">Web:</span> <span class="value">www.thekelp.com</span></span>
      </div>
    </footer>
  </section>

</body>
</html>
```